Quarvelon stickers design for our main topics (for example: agile and Kanban)

We are looking for sticker design, that will reflect our cooperate identity and can be used for the different topics in our company. We would like to start with our Agile Coaching Offers with a Kanban Sticker saying "stop starting, start finishing", A bad example can be find in the file upload ;)
Check out our homepage to get a feeling for the cooperate identity (www.quarvelon-beispiel.ch)

Target Market(s)

Customers and trainees from our trainings

Industry/Entity Type

Consulting

Colors
0355a3
fbed22

Requirements
Must have
• a cool design thats fits to our customer design
the 2 lines can be changed for future stickers ... like in the example "stop starting, start finishing" and "we show you how"
Nice to have
• -
Should not have
• -

```html
<!DOCTYPE html>
<html lang="de">
<head>
<meta charset="utf-8">
<title>Quarvelon Sticker – Stop Starting, Start Finishing</title>
<link rel="stylesheet" href="https://fonts.googleapis.com/css2?family=Figtree:wght@300;700;800&display=swap">
<style>
  :root {
    --brand-blue: #0433f0;
    --brand-yellow: #fbfaa0;
    --ink: #111111;
    --paper: #ffffff;
  }
  * { box-sizing: border-box; margin: 0; padding: 0; }
  html, body {
    width: 1200px;
    height: 1200px;
    overflow: hidden;
    background: var(--paper);
  }
  .canvas {
    position: relative;
    width: 1200px;
    height: 1200px;
    font-family: "Figtree", "Helvetica Neue", Arial, sans-serif;
  }
  .sticker {
    position: absolute;
    left: 83px;
    width: 1020px;
    height: 294px;
    border: 19px solid var(--brand-yellow);
    border-radius: 56px;
    background: var(--paper);
    overflow: hidden;
  }
  .sticker--yellow { top: 252px; border-color: var(--brand-yellow); }
  .sticker--blue { top: 640px; border-color: var(--brand-blue); }

  .topic-visual {
    position: absolute;
    left: 24px;
    top: -3px;
    width: 460px;
    height: 260px;
    background: linear-gradient(115deg, var(--brand-yellow) 0%, var(--brand-yellow) 42%, var(--brand-blue) 58%, var(--brand-blue) 100%);
  }
  .topic-stop {
    position: absolute;
    left: 70px;
    top: 60px;
    color: var(--brand-blue);
    font-weight: 700;
    font-size: 40px;
    line-height: 0.9;
    text-align: center;
    transform: rotate(-27deg);
  }
  .topic-finish {
    position: absolute;
    left: 240px;
    top: 115px;
    color: var(--brand-yellow);
    font-weight: 700;
    font-size: 40px;
    line-height: 0.92;
    text-align: center;
  }
  .tagline {
    position: absolute;
    left: 533px;
    top: 52px;
    color: var(--brand-blue);
    font-weight: 700;
    font-size: 43px;
    letter-spacing: 0.2px;
    white-space: nowrap;
  }
  .company-name {
    position: absolute;
    left: 688px;
    top: 112px;
    color: var(--ink);
    font-weight: 300;
    font-size: 43px;
    white-space: nowrap;
  }
</style>
</head>
<body>
<main class="canvas">
  <section class="sticker sticker--yellow">
    <div class="topic-visual" role="img" aria-label="Hand-drawn overlapping yellow and blue sticky notes"></div>
    <p class="topic-stop">STOP<br>STARTING</p>
    <p class="topic-finish">START<br>FINISHING</p>
    <p class="tagline">We show you how...</p>
    <p class="company-name">Quarvelon ag</p>
  </section>

  <section class="sticker sticker--blue">
    <div class="topic-visual" role="img" aria-label="Hand-drawn overlapping yellow and blue sticky notes"></div>
    <p class="topic-stop">STOP<br>STARTING</p>
    <p class="topic-finish">START<br>FINISHING</p>
    <p class="tagline">We show you how...</p>
    <p class="company-name">Quarvelon ag</p>
  </section>
</main>
</body>
</html>
```